New Business Card

We need to refresh our business cards. We designed these ourselves and we have no graphic design experience. We would like to find a new business card design that is professional and unique. We are an auto finance company. Feel free to play with the logo, but we would like to keep the eye very present on the card. Our corporate colors are green, grey, and white.
Green - RGB - 168,215,27; HEX - #AADD22
Grey - RGB - 196,196,196; HEX - #C4C4C4
Updates
Need to upload the vector file to finalize the project. The last logo was for a jpeg that didn't stretch well.
Industry/Entity Type
Financial Service
Contact Information for Business Card
Honestly don't know...I need your help!

```html
<!DOCTYPE html>
<html lang="en">
<head>
<meta charset="utf-8">
<title>Brightline Capital — Business Card</title>
<link rel="stylesheet" href="https://fonts.googleapis.com/css2?family=Arimo:wght@400;700&display=swap">
<style>
  :root {
    --brand-green: #aadd22;
    --brand-grey: #c4c4c4;
    --card-white: #ffffff;
    --card-black: #050505;
    --ink: #111111;
    --stage: #ecebe8;
    --icon-ring: #2a2a2a;
  }
  * { box-sizing: border-box; margin: 0; padding: 0; }
  html, body {
    width: 1200px;
    height: 800px;
    overflow: hidden;
    background: var(--stage);
    font-family: "Arimo", Arial, sans-serif;
  }
  .stage {
    position: relative;
    width: 1200px;
    height: 800px;
  }
  .card {
    position: absolute;
    top: 252px;
    width: 520px;
    height: 297px;
    box-shadow: 0 6px 18px rgba(0,0,0,0.18);
    overflow: hidden;
  }
  .card--back {
    left: 60px;
    background: var(--card-black);
    display: flex;
    align-items: center;
    justify-content: center;
  }
  .card--front {
    left: 620px;
    background: var(--card-white);
  }

  .brand {
    display: flex;
    align-items: center;
    gap: 12px;
    color: var(--brand-green);
    font-weight: 700;
    white-space: nowrap;
  }
  .brand__dot {
    border-radius: 50%;
    background: currentColor;
    flex: none;
  }
  .card--back .brand {
    color: var(--brand-grey);
    font-size: 34px;
  }
  .card--back .brand__dot { width: 30px; height: 30px; }

  .card--front .brand {
    position: absolute;
    left: 36px;
    top: 128px;
    font-size: 24px;
  }
  .card--front .brand__dot { width: 22px; height: 22px; }

  .accent-line {
    position: absolute;
    inset: 0;
    width: 520px;
    height: 297px;
  }

  .holder {
    position: absolute;
    right: 32px;
    top: 56px;
    text-align: right;
  }
  .holder__name {
    font-size: 22px;
    font-weight: 700;
    color: var(--ink);
    letter-spacing: 0.5px;
  }
  .holder__title {
    font-size: 14px;
    color: var(--brand-green);
    margin-top: 2px;
  }

  .contact__text {
    position: absolute;
    font-size: 13px;
    color: var(--ink);
    white-space: nowrap;
    line-height: 1;
  }
  .contact__text--phone { left: 352px; top: 116px; }
  .contact__text--email { left: 326px; top: 150px; }
  .contact__text--web   { left: 299px; top: 183px; }
</style>
</head>
<body>
<main class="stage">

  <section class="card card--back" aria-label="Card back">
    <div class="brand"><span class="brand__dot"></span>Brightline Capital</div>
  </section>

  <section class="card card--front" aria-label="Card front">
    <svg class="accent-line" viewBox="0 0 520 297" aria-hidden="true">
      <polyline points="340,0 350,95 245,230" fill="none" stroke="var(--brand-green)" stroke-width="2"/>

      <g class="contact-icon contact-icon--phone" transform="translate(329,122)">
        <circle r="12" fill="var(--brand-green)" stroke="var(--icon-ring)" stroke-width="2"/>
        <path d="M-4,-6 l3,0 l1,3 l-2,1.5 q1.5,3 4,4.5 l1.5,-2 l3,1 l0,3 q-1,1.5 -3,1.5 q-9,-2 -10,-10 q0,-2 2.5,-2.5z" fill="var(--ink)"/>
      </g>
      <g class="contact-icon contact-icon--email" transform="translate(303,156)">
        <circle r="12" fill="var(--brand-green)" stroke="var(--icon-ring)" stroke-width="2"/>
        <rect x="-6.5" y="-4.5" width="13" height="9" fill="var(--ink)"/>
        <polyline points="-6.5,-4.5 0,1 6.5,-4.5" fill="none" stroke="var(--brand-green)" stroke-width="1.2"/>
      </g>
      <g class="contact-icon contact-icon--web" transform="translate(276,189)">
        <circle r="12" fill="var(--brand-green)" stroke="var(--icon-ring)" stroke-width="2"/>
        <g fill="none" stroke="var(--ink)" stroke-width="1.2">
          <circle r="6.5"/>
          <ellipse rx="3" ry="6.5"/>
          <line x1="-6.5" y1="0" x2="6.5" y2="0"/>
          <line x1="-5.5" y1="-3.3" x2="5.5" y2="-3.3"/>
          <line x1="-5.5" y1="3.3" x2="5.5" y2="3.3"/>
        </g>
      </g>
    </svg>

    <div class="brand"><span class="brand__dot"></span>Brightline Capital</div>

    <div class="holder">
      <p class="holder__name">JOHN DOE</p>
      <p class="holder__title">Manager</p>
    </div>

    <p class="contact__text contact__text--phone">555.014.2290</p>
    <p class="contact__text contact__text--email">email@brightlinecap.com</p>
    <p class="contact__text contact__text--web">www.brightlinecap.com</p>
  </section>

</main>
</body>
</html>
```